book cover

this is a book titled "the silver compass" it has stories from real people about how they made their dreams come true, have overcome problems .... they use "to think is to create" meaning if you reallly want something you have to picture it in your mind and think on that. kind of like a vision board

```html
<!DOCTYPE html>
<html lang="en">
<head>
<meta charset="UTF-8">
<title>The Silver Compass — Book Cover</title>
<link rel="stylesheet" href="https://fonts.googleapis.com/css2?family=Alegreya+Sans:wght@400&family=Tinos:wght@700&display=swap">
<style>
  :root {
    --deep-navy: #0b1830;
    --night-blue: #14305e;
    --royal-blue: #1f5fb8;
    --sky-blue: #3fa9e6;
    --pale-cyan: #9fd8f2;
    --mist: #d9dde3;
    --sea-green: #1f6b5a;
    --title-white: #ffffff;
  }
  * { margin: 0; padding: 0; box-sizing: border-box; }
  html, body {
    width: 800px;
    height: 1200px;
    overflow: hidden;
    background: var(--deep-navy);
  }
  .cover {
    position: relative;
    width: 800px;
    height: 1200px;
    overflow: hidden;
    background: linear-gradient(180deg, var(--night-blue) 0%, var(--royal-blue) 22%, #2a3f78 45%, #1b2a4a 62%, var(--deep-navy) 100%);
  }
  .cover-art {
    position: absolute;
    inset: 0;
    width: 800px;
    height: 1200px;
  }
  .cover-title {
    position: absolute;
    left: 0;
    top: 610px;
    width: 800px;
    font-family: "Alegreya Sans", "Trebuchet MS", sans-serif;
    font-weight: 400;
    font-size: 124px;
    line-height: 96px;
    color: var(--title-white);
    letter-spacing: -1px;
  }
  .cover-title span { display: block; }
  .title-line-1 { padding-left: 224px; }
  .title-line-2 { padding-left: 146px; }
  .title-line-3 { padding-left: 256px; }
  .cover-author {
    position: absolute;
    right: 44px;
    bottom: 42px;
    font-family: "Tinos", "Times New Roman", serif;
    font-weight: 700;
    font-size: 28px;
    color: var(--mist);
  }
</style>
</head>
<body>
<main class="cover">
  <svg class="cover-art" viewBox="0 0 800 1200" xmlns="http://www.w3.org/2000/svg">
    <defs>
      <linearGradient id="band-light" x1="0" y1="0" x2="1" y2="0">
        <stop offset="0" stop-color="#f1e6dc" stop-opacity="0.95"/>
        <stop offset="0.45" stop-color="#b9c3d6" stop-opacity="0.6"/>
        <stop offset="1" stop-color="#5d7fb5" stop-opacity="0"/>
      </linearGradient>
      <linearGradient id="band-cyan" x1="0" y1="0" x2="1" y2="0">
        <stop offset="0" stop-color="#3fa9e6" stop-opacity="0.2"/>
        <stop offset="0.6" stop-color="#7fd0f5" stop-opacity="0.8"/>
        <stop offset="1" stop-color="#3fa9e6" stop-opacity="0.3"/>
      </linearGradient>
      <linearGradient id="band-sea" x1="0" y1="0" x2="1" y2="0">
        <stop offset="0" stop-color="#1f6b5a" stop-opacity="0.9"/>
        <stop offset="1" stop-color="#1f5fb8" stop-opacity="0.4"/>
      </linearGradient>
      <radialGradient id="eye-area" cx="0.5" cy="0.5" r="0.5">
        <stop offset="0" stop-color="#5f7fa8" stop-opacity="0.75"/>
        <stop offset="0.6" stop-color="#4a6ea6" stop-opacity="0.4"/>
        <stop offset="1" stop-color="#3a62a8" stop-opacity="0"/>
      </radialGradient>
      <radialGradient id="glow" cx="0.5" cy="0.5" r="0.5">
        <stop offset="0" stop-color="#ffffff" stop-opacity="0.35"/>
        <stop offset="1" stop-color="#ffffff" stop-opacity="0"/>
      </radialGradient>
    </defs>

    <path d="M0 0 H800 V110 C600 60 300 40 0 90 Z" fill="#3fa9e6" opacity="0.35"/>
    <path d="M0 70 C250 20 560 40 800 150 V210 C560 110 280 80 0 130 Z" fill="url(#band-cyan)" opacity="0.6"/>

    <ellipse role="img" aria-label="Soft close-up photograph of a human eye, fading into the blue sky" cx="420" cy="320" rx="260" ry="150" fill="url(#eye-area)"/>

    <path d="M0 440 C220 410 520 300 800 150 V230 C560 370 260 480 0 500 Z" fill="url(#band-cyan)" opacity="0.55"/>
    <path d="M0 470 C200 460 420 500 800 470 V560 C460 600 220 560 0 620 Z" fill="url(#band-light)"/>
    <path d="M0 640 C240 600 520 640 800 600 V650 C520 690 240 650 0 700 Z" fill="#9fd8f2" opacity="0.18"/>

    <circle cx="430" cy="580" r="130" fill="url(#glow)"/>
    <circle cx="560" cy="610" r="90" fill="url(#glow)"/>
    <circle cx="690" cy="540" r="150" fill="url(#glow)" opacity="0.7"/>

    <path d="M0 930 C260 880 560 880 800 930 V980 C540 940 260 950 0 1000 Z" fill="#3fa9e6" opacity="0.45"/>
    <path d="M0 1000 C260 960 560 980 800 1010 V1060 C540 1040 260 1030 0 1070 Z" fill="url(#band-sea)"/>
    <path d="M0 1080 C300 1050 560 1070 800 1100 V1200 H0 Z" fill="#070f1f" opacity="0.85"/>
  </svg>

  <h1 class="cover-title">
    <span class="title-line-1">The</span>
    <span class="title-line-2">Silver</span>
    <span class="title-line-3">Compass</span>
  </h1>
  <p class="cover-author">Writer’s Name</p>
</main>
</body>
</html>
```